Project: Stationary for product web site
Stationary for product web site - Automotive
Bright & Fun-filled
Dorian Feltz
Directory of Marketing
7213 W. Pellam Avenue # 208 Lauderhill, FL, 33329
dorian.feltz@quillmarkgear.com
Xpert Xpert

```html
<!DOCTYPE html>
<html lang="en">
<head>
<meta charset="utf-8">
<title>Kestova Business Cards</title>
<link rel="stylesheet" href="https://fonts.googleapis.com/css2?family=Open+Sans:wght@400;600;700;800&display=swap">
<style>
  :root {
    --brand-blue: #1d3f9e;
    --brand-orange: #f07a1c;
    --ink: #3a3a3a;
    --card: #ffffff;
    --backdrop: #e4e5e8;
  }
  * { margin: 0; padding: 0; box-sizing: border-box; }
  html, body { width: 1200px; height: 902px; overflow: hidden; }
  body {
    background: var(--backdrop);
    font-family: "Open Sans", Arial, sans-serif;
    position: relative;
  }
  .card {
    position: absolute;
    left: 250px;
    width: 700px;
    height: 400px;
    background: var(--card);
    border-radius: 8px;
    box-shadow: 0 6px 18px rgba(0,0,0,0.15);
    overflow: hidden;
  }
  .card--back { top: 34px; }
  .card--front { top: 468px; }

  .brand {
    display: flex;
    align-items: center;
    gap: 12px;
    font-weight: 800;
    color: var(--brand-blue);
    letter-spacing: 1px;
  }
  .brand__dot {
    width: 22px; height: 22px;
    border-radius: 50%;
    background: var(--brand-orange);
  }
  .card--back .brand {
    position: absolute;
    left: 0; right: 0; top: 130px;
    justify-content: center;
    font-size: 64px;
  }
  .card--back .website {
    position: absolute;
    left: 0; right: 0; top: 238px;
    text-align: center;
    font-size: 20px;
    color: var(--ink);
    letter-spacing: 0.5px;
  }

  .card--front .brand {
    position: absolute;
    left: 40px; top: 50px;
    font-size: 46px;
  }
  .holder {
    position: absolute;
    right: 44px; top: 48px;
    text-align: right;
  }
  .holder__name {
    font-size: 24px;
    font-weight: 600;
    color: var(--brand-blue);
  }
  .holder__title {
    font-size: 16px;
    color: var(--brand-orange);
    margin-top: 2px;
  }
  .contact {
    position: absolute;
    right: 36px; top: 146px;
    list-style: none;
    text-align: right;
    font-size: 15px;
    color: var(--ink);
    line-height: 23px;
  }
  .contact li {
    display: flex;
    justify-content: flex-end;
    align-items: center;
    gap: 9px;
  }
  .contact svg { width: 13px; height: 13px; fill: var(--ink); flex: none; }
  .swoosh { position: absolute; left: 0; top: 0; width: 700px; height: 400px; }
</style>
</head>
<body>
  <section class="card card--back">
    <div class="brand"><span class="brand__dot"></span>KESTOVA</div>
    <p class="website">www.quillmarkgear.com</p>
  </section>

  <section class="card card--front">
    <svg class="swoosh" viewBox="0 0 700 400" aria-hidden="true">
      <path d="M0,268 C200,256 430,316 700,360" fill="none" stroke="var(--brand-blue)" stroke-width="12"/>
      <path d="M0,290 C200,280 430,334 700,376 L700,400 L0,400 Z" fill="var(--brand-orange)"/>
      <path d="M0,350 C220,338 450,374 700,400 L0,400 Z" fill="var(--brand-blue)"/>
    </svg>

    <div class="brand"><span class="brand__dot"></span>KESTOVA</div>

    <div class="holder">
      <p class="holder__name">Dorian Feltz</p>
      <p class="holder__title">Director of Marketing</p>
    </div>

    <ul class="contact">
      <li>555 204 7713
        <svg viewBox="0 0 16 16"><path d="M3.6 1.2l2.3 2.6-1.3 1.9c.9 2 2.6 3.7 4.6 4.6l1.9-1.3 2.6 2.3-1.4 2.3C7 13.2 2.8 9 1.3 2.6z"/></svg>
      </li>
      <li>555 204 7714
        <svg viewBox="0 0 16 16"><path d="M4 1h8v4H4zM1 6h14v7h-3v2H4v-2H1zM5 10v4h6v-4z"/></svg>
      </li>
      <li>dorian.feltz@quillmarkgear.com
        <svg viewBox="0 0 16 16"><path d="M1 3h14v10H1zM2.5 4.5v.4L8 9l5.5-4.1v-.4z"/></svg>
      </li>
      <li>7213 W. Pellam Avenue # 208 Lauderhill, FL, 33329
        <svg viewBox="0 0 16 16"><path d="M8 1a5 5 0 0 0-5 5c0 3.5 5 9 5 9s5-5.5 5-9a5 5 0 0 0-5-5zm0 7a2 2 0 1 1 0-4 2 2 0 0 1 0 4z"/></svg>
      </li>
    </ul>
  </section>
</body>
</html>
```